App Design Project

We are building an app and looking for design help on an existing template. We will also need a style guide. For more information, there is a website which outlines the assignment with visuals. Go here:

http://www.brivalora.com/

Industry/Entity Type

Building

```html
<!DOCTYPE html>
<html lang="en">
<head>
<meta charset="utf-8">
<title>Activities – App Screen</title>
<link rel="stylesheet" href="https://fonts.googleapis.com/css2?family=Open+Sans:wght@400;600;700&display=swap">
<style>
  :root{
    --page:#e9e9e9;
    --status:#000000;
    --header-top:#d4484a;
    --header-bottom:#a81f20;
    --dark-btn-top:#3a3a3a;
    --dark-btn-bottom:#141414;
    --cream-band:#fbe5c1;
    --cyan-top:#3fd3ea;
    --cyan-bottom:#0c9cb8;
    --cyan-text:#17677b;
    --wood:#d9955a;
    --wood-dark:#c9844a;
    --paper:#f3f0e9;
    --paper-edge:#dcd6ca;
    --title:#1b1b1b;
    --body:#8c8c8c;
    --caption:#7a7a7a;
    --green-top:#35c25a;
    --green-bottom:#138a36;
    --tabbar:#2a2a2a;
    --orange-top:#f0a050;
    --orange-bottom:#cf6d1f;
    --white:#ffffff;
  }
  *{box-sizing:border-box;margin:0;padding:0}
  html,body{width:1200px;height:2345px;overflow:hidden;background:var(--page)}
  body{position:relative;font-family:"Open Sans",sans-serif}

  .screen{
    position:absolute;left:101px;top:418px;width:640px;height:960px;
    transform:scale(1.5797);transform-origin:0 0;overflow:hidden;background:var(--wood);
  }

  .status-bar{position:absolute;left:0;top:0;width:640px;height:40px;background:var(--status);color:var(--white);
    font-weight:600;font-size:24px;line-height:40px}
  .status-bar .signal{position:absolute;left:8px;top:10px}
  .status-bar .carrier{position:absolute;left:54px}
  .status-bar .time{position:absolute;left:0;width:640px;text-align:center}
  .status-bar .clock{position:absolute;left:556px;top:10px}
  .status-bar .battery{position:absolute;left:592px;top:11px}

  .nav-bar{position:absolute;left:0;top:40px;width:640px;height:82px;
    background:linear-gradient(var(--header-top),var(--header-bottom));border-bottom:2px solid #7d1414}
  .nav-title{position:absolute;left:0;width:640px;top:18px;text-align:center;color:var(--white);
    font-weight:700;font-size:33px;letter-spacing:.5px}
  .dark-btn{position:absolute;top:18px;height:46px;border-radius:8px;color:var(--white);font-weight:600;font-size:21px;
    line-height:44px;text-align:center;background:linear-gradient(var(--dark-btn-top),var(--dark-btn-bottom));
    border:1px solid #000;box-shadow:0 1px 0 rgba(255,255,255,.25)}
  .dark-btn.search{left:18px;width:102px}
  .dark-btn.sort{left:548px;width:72px}

  .filter-band{position:absolute;left:0;top:122px;width:640px;height:82px;background:var(--cream-band);
    box-shadow:0 3px 4px rgba(0,0,0,.25)}
  .cyan-btn{position:absolute;height:46px;border-radius:7px;color:var(--cyan-text);font-size:22px;line-height:44px;
    text-align:center;background:linear-gradient(var(--cyan-top),var(--cyan-bottom));border:1px solid #0a7f96}
  .filter-band .cyan-btn{top:16px;width:151px}
  .filter-band .all{left:35px}
  .filter-band .people{left:235px}
  .filter-band .groups{left:445px}

  .wood{position:absolute;left:0;top:204px;width:640px;height:676px;
    background:repeating-linear-gradient(90deg,var(--wood) 0 38px,var(--wood-dark) 38px 40px,var(--wood) 40px 72px,#d08c50 72px 80px)}
  .card-stack{position:absolute;left:16px;top:0;width:606px;height:624px;border-radius:0 0 14px 14px;
    background:var(--paper);border:1px solid var(--paper-edge);box-shadow:0 3px 0 var(--paper),0 4px 0 var(--paper-edge),0 7px 0 var(--paper),0 8px 0 var(--paper-edge),0 10px 6px rgba(0,0,0,.3)}

  .activity{position:absolute;left:0;width:640px;height:160px}
  .thumb{position:absolute;left:45px;top:0;width:124px;height:122px;background:var(--white);
    box-shadow:0 1px 3px rgba(0,0,0,.45);padding:8px}
  .thumb .photo{width:100%;height:100%;background:linear-gradient(#3a3a3a,#222)}
  .caption{position:absolute;left:45px;width:106px;top:128px;text-align:center;color:var(--caption);
    font-weight:700;font-size:16px}
  .activity-title{position:absolute;left:190px;top:-4px;font-weight:600;font-size:27px;color:var(--title)}
  .activity-body{position:absolute;left:190px;top:32px;width:380px;font-size:16.5px;line-height:27px;color:var(--body)}
  .next-tab{position:absolute;left:579px;top:10px;width:53px;height:90px;border-radius:3px 0 0 3px;
    background:linear-gradient(90deg,var(--green-top),var(--green-bottom));box-shadow:0 2px 3px rgba(0,0,0,.35)}
  .next-tab span{position:absolute;left:50%;top:50%;transform:translate(-50%,-50%) rotate(-90deg);
    color:var(--white);font-weight:700;font-size:20px;letter-spacing:1px}

  .tab-bar{position:absolute;left:0;top:880px;width:640px;height:80px;background:var(--tabbar);border-top:2px solid #111}
  .tab-bar .btn{position:absolute;top:18px;height:46px;border-radius:7px;font-size:22px;line-height:44px;text-align:center}
  .orange-btn{color:var(--white);background:linear-gradient(var(--orange-top),var(--orange-bottom));border:1px solid #9d4d12}
  .tab-bar .search{left:18px;width:100px}
  .tab-bar .new-post{left:136px;width:139px}
  .tab-bar .msgs{left:296px;width:87px}
  .tab-bar .alerts{left:412px;width:92px}
  .tab-bar .more{left:532px;width:92px}
</style>
</head>
<body>
  <main class="screen">
    <div class="status-bar">
      <svg class="signal" width="40" height="20" viewBox="0 0 40 20" aria-hidden="true">
        <rect x="0" y="16" width="5" height="4" fill="#fff"/>
        <rect x="7" y="12" width="5" height="8" fill="#fff"/>
        <rect x="14" y="8" width="5" height="12" fill="#fff"/>
        <rect x="21" y="4" width="5" height="16" fill="#fff"/>
        <rect x="28" y="0" width="5" height="20" fill="#fff"/>
      </svg>
      <span class="carrier">NIMBUS &nbsp;3G</span>
      <span class="time">4:20 PM</span>
      <svg class="clock" width="20" height="20" viewBox="0 0 20 20" aria-hidden="true">
        <circle cx="10" cy="10" r="9" fill="#fff"/>
        <path d="M10 4v6h-4" stroke="#000" stroke-width="2" fill="none"/>
      </svg>
      <svg class="battery" width="42" height="19" viewBox="0 0 42 19" aria-hidden="true">
        <rect x="1" y="1" width="36" height="17" rx="2" fill="none" stroke="#fff" stroke-width="2"/>
        <rect x="4" y="4" width="30" height="11" fill="#fff"/>
        <rect x="38" y="6" width="3" height="7" fill="#fff"/>
      </svg>
    </div>

    <header class="nav-bar">
      <div class="dark-btn search">Search</div>
      <h1 class="nav-title">ACTIVITIES</h1>
      <div class="dark-btn sort">Sort</div>
    </header>

    <nav class="filter-band">
      <div class="cyan-btn all">Search All</div>
      <div class="cyan-btn people">People</div>
      <div class="cyan-btn groups">Groups</div>
    </nav>

    <section class="wood">
      <div class="card-stack"></div>

      <article class="activity" style="top:36px">
        <div class="thumb"><div class="photo" role="img" aria-label="Member avatar"></div></div>
        <div class="caption">Nancy 14</div>
        <h2 class="activity-title">Midnight Picture Show</h2>
        <p class="activity-body">Lorem ipsum dolor sit amet, consectetuer adipiscing elit. Aenean commodo ligula eget dolor. Aenean massa.</p>
        <div class="next-tab"><span>NEXT</span></div>
      </article>

      <article class="activity" style="top:236px">
        <div class="thumb"><div class="photo" role="img" aria-label="Member avatar"></div></div>
        <div class="caption">Nancy 14</div>
        <h2 class="activity-title">Midnight Picture Show</h2>
        <p class="activity-body">Lorem ipsum dolor sit amet, consectetuer adipiscing elit. Aenean commodo ligula eget dolor. Aenean massa.</p>
        <div class="next-tab"><span>NEXT</span></div>
      </article>

      <article class="activity" style="top:446px">
        <div class="thumb"><div class="photo" role="img" aria-label="Member avatar"></div></div>
        <div class="caption">Nancy 14</div>
        <h2 class="activity-title">Midnight Picture Show</h2>
        <p class="activity-body">Lorem ipsum dolor sit amet, consectetuer adipiscing elit. Aenean commodo ligula eget dolor. Aenean massa.</p>
        <div class="next-tab"><span>NEXT</span></div>
      </article>
    </section>

    <footer class="tab-bar">
      <div class="btn orange-btn search">Search</div>
      <div class="btn cyan-btn new-post">New Post</div>
      <div class="btn orange-btn msgs">MSGS</div>
      <div class="btn orange-btn alerts">Alerts</div>
      <div class="btn orange-btn more">More</div>
    </footer>
  </main>
</body>
</html>
```